Health and Wellbeing online Shop

I have attached a specification, however in summary this is a new business startup selling vitamins and supplements.

We need a web design for new wellbeing website, selling high end vitamins, supplements and nootropics. Therefore I need a simple eCommerce solution .

I need the website to look very different to other websites on the market. The more creative the better. It should look fresh elegant and simple. The criteria for products being on my site is that they have great reviews and they have been scientifically tested.

You will need the option of being able to log into an account, either through pagebook, snoople, chirpnet, Pixogram or create an account with email. For accounts, users will need the facility to reset passwords, see previous orders, track current order, and maintain favourites.

It should be PC, mobile and tablet friendly.

Look and Feel

It should be an elegant, modern, professional, trendy, unisex website. It should look clean and calm. Am happy to try interesting and slightly unusual designs. I would also like to have chat functionality, either powered by volKAtalk or by Bax 61.

Websites I like are
https://www.corvan-radiance.co.uk/
https://www.plainnutrients.co.uk/
http://www.lumadermis.com/

PLEASE DO USE YOUR KNOWELDGE OF WHAT WORKS FOR WEB DESIGN. YOU’RE THE EXPERT AND NEED YOUR EXPERTISE. CARTE BLANCHE TO DESIGN AS YOU SEE FIT. Please be creative, I need my site to stand out from the crowd.

Target Market(s)
Middle aged women are our most common client, however, younger patients, both male and female, will often visit the site. In summary, I would like the site to appeal to all age brackets.

Industry/Entity Type
Business

Coding
Coded - Design and coding required

Number of Pages Required
5 pages
Updates

I would like more designs. I was expecting 75+ Designs to choose from as per the package I paid for.

Target Market(s)

Industry/Entity Type

Health And Wellness

Coding

Number of Pages Required

5+ page

Requirements
Must have
• Creative design

```html
<!DOCTYPE html>
<html lang="en">
<head>
<meta charset="utf-8">
<title>Verdalis — Vitamins &amp; Nootropics</title>
<link rel="stylesheet" href="https://fonts.googleapis.com/css2?family=Libre+Caslon+Text:wght@400;700&display=swap">
<style>
:root{
  --ink:#111;
  --muted:#6f6f6f;
  --rule:#8c8c8c;
  --paper:#fff;
  --backdrop:#fff;
  --footer:#8b8b8b;
  --hero-grey-a:#e4e6ea;
  --hero-grey-b:#c9ccd2;
  --mat:#6b5470;
  --bottle-a:#f07a30;
  --bottle-b:#d95a1c;
  --cap:#1e1a1a;
}
*{box-sizing:border-box;margin:0;padding:0}
html,body{width:1200px;height:1200px;overflow:hidden;background:var(--backdrop)}
body{font-family:"Libre Caslon Text",Georgia,serif;color:var(--ink)}
.page{position:absolute;left:231px;top:0;width:745px;height:1160px;background:var(--paper);box-shadow:0 6px 14px rgba(0,0,0,.45)}
.abs{position:absolute}

/* nav */
.top-nav{position:absolute;left:0;top:0;width:100%;height:24px;border-bottom:1px solid var(--rule)}
.top-nav a{position:absolute;top:7px;font-size:6.6px;letter-spacing:.2px;color:var(--ink);text-decoration:none}

/* hero */
.hero{position:absolute;left:54px;top:24px;width:637px;height:208px}
.hero svg{position:absolute;left:0;top:0}
.hero-title{position:absolute;right:0;top:58px;text-align:right;font-size:19.5px;line-height:21.8px;font-weight:400}
.btn{display:inline-block;background:var(--ink);color:#fff;border-radius:20px;text-align:center;text-decoration:none}
.btn-enter{position:absolute;right:0;top:175px;width:89px;height:16px;line-height:16px;font-size:8.5px}

/* sidebar */
.sidebar{position:absolute;left:54px;width:87px}
.filter-head{display:flex;align-items:center;justify-content:space-between;height:15px;font-size:10.5px;color:#555}
.filter-head span{border-bottom:1px solid var(--rule);line-height:13px;width:71px;white-space:nowrap}
.filter-list{list-style:none}
.filter-list li{height:15px;line-height:14px;font-size:8.6px;color:#666;border-bottom:1px solid var(--rule);white-space:nowrap}

/* products */
.section-title{position:absolute;left:171px;font-size:14.5px;font-weight:400;border-bottom:1px solid var(--ink);line-height:18px}
.product-row{position:absolute;left:171px;width:520px;display:flex}
.product-card{position:absolute;width:100px;margin-left:-50px;text-align:center}
.product-photo{width:40px;height:75px;margin:0 auto;border-radius:8px 8px 6px 6px;background:linear-gradient(180deg,var(--cap) 0 14%,var(--bottle-a) 14%,var(--bottle-b) 100%)}
.product-name{margin-top:10px;font-size:6.7px;line-height:7px}
.product-stars{margin-top:6px;font-size:8px;letter-spacing:.5px;line-height:10px}
.product-price{margin-top:3px;font-size:7.5px;line-height:10px}
.product-price small{font-size:6.5px}
.btn-cart{margin-top:5px;width:56px;height:10px;line-height:10px;font-size:5.5px;font-weight:700}
.see-more{position:absolute;left:171px;width:520px;height:16px;border-top:1px solid var(--ink);border-bottom:1px solid var(--ink);text-align:center;font-size:8.2px;line-height:15px}

/* about */
.about{position:absolute;left:171px;top:730px;width:520px;height:192px;background:linear-gradient(180deg,#e3e3e3,#d3d3d3 60%,#c9c9c9);text-align:center}
.about-title{display:inline-block;margin-top:10px;font-size:14.5px;font-weight:400;line-height:18px;border-bottom:1px solid var(--ink)}
.about p{margin:12px auto 0;width:490px;font-size:8.1px;line-height:12px}
.about p+p{margin-top:0}
.btn-learn{position:absolute;left:228px;top:168px;width:65px;height:11px;line-height:11px;font-size:5.6px;font-weight:700}

/* contact */
.contact{position:absolute;left:171px;top:936px;width:520px;text-align:center;font-size:8.2px;line-height:12px}
.contact-title{display:inline-block;font-size:14.5px;font-weight:400;line-height:18px;border-bottom:1px solid var(--ink);margin-left:8px}
.btn-message{position:absolute;left:650px;top:1051px;width:95px;height:19px;line-height:19px;font-size:7px;background:var(--ink);color:#fff;border-radius:10px 0 0 10px;text-align:center}

/* footer */
.site-footer{position:absolute;left:0;top:1081px;width:100%;height:79px;background:var(--footer);color:#fff}
.footer-col{position:absolute;top:12px}
.footer-col h4{font-weight:400;font-size:8.6px;display:inline-block;border-bottom:1px solid #fff;line-height:11px;margin-bottom:4px}
.footer-col ul{list-style:none}
.footer-col li{font-size:5.3px;line-height:9px}
</style>
</head>
<body>
<div class="page">

  <nav class="top-nav">
    <a style="left:349px">VITAMINS</a>
    <a style="left:424px">NOOTROPICS</a>
    <a style="left:514px">ABOUT US</a>
    <a style="left:591px">CONTACT US</a>
  </nav>

  <header class="hero">
    <svg width="637" height="208" viewBox="0 0 637 208" role="img" aria-label="Woman in black sportswear doing a kneeling leg-lift stretch on a yoga mat in a bright studio">
      <defs>
        <linearGradient id="heroFill" x1="0" y1="0" x2="1" y2="1">
          <stop offset="0" stop-color="var(--hero-grey-a)"/>
          <stop offset="0.7" stop-color="var(--hero-grey-b)"/>
          <stop offset="1" stop-color="var(--mat)"/>
        </linearGradient>
      </defs>
      <polygon points="0,0 525,0 319,208 0,208" fill="url(#heroFill)"/>
    </svg>
    <h1 class="hero-title">Welcome to<br>your favorite one-stop<br>Shop for all your<br>Vitamin &amp; Nootropics<br>Needs</h1>
    <a class="btn btn-enter">Enter Shop</a>
  </header>

  <aside class="sidebar" style="top:253px">
    <div class="filter-head"><span>Our Categories</span>
      <svg width="9" height="9" viewBox="0 0 10 10"><circle cx="5" cy="5" r="4.3" fill="none" stroke="#333" stroke-width=".8"/><path d="M3 6 5 4 7 6" fill="none" stroke="#333" stroke-width=".8"/></svg></div>
    <ul class="filter-list">
      <li>Amino Acids</li><li>Antioxidants</li><li>Cannabis Oil CBD</li><li>Chondroitin</li><li>Coenzyme Q10</li><li>Cod Liver Oil</li><li>Essential Fatty Acids</li><li>Evening Primrose Oils</li><li>Fish Oils</li><li>Glucosamine</li><li>Herbal / Botanical</li><li>Minerals</li><li>MultiVitamins</li><li>Omega-3</li><li>Pregnancy</li><li>Probiotics</li><li>Vegan</li><li>Vegeterian</li><li>Vitamin B</li><li>Vitamin C</li><li>Vitamin D</li><li>Vitamin E</li><li>Vitamin K</li>
    </ul>
  </aside>

  <aside class="sidebar" style="top:633px">
    <div class="filter-head"><span>Interest</span>
      <svg width="9" height="9" viewBox="0 0 10 10"><circle cx="5" cy="5" r="4.3" fill="none" stroke="#333" stroke-width=".8"/><path d="M3 6 5 4 7 6" fill="none" stroke="#333" stroke-width=".8"/></svg></div>
    <ul class="filter-list">
      <li>Ageing</li><li>Bone Health</li><li>Children's Health</li><li>Circulation</li><li>Digestive Health</li><li>Energy</li><li>Eye Health</li><li>Heart Health</li><li>Immune System</li><li>Joints &amp; Muscles</li><li>Memory</li><li>Menopause</li><li>Men's Health</li><li>Skin / Hair / Beauty</li><li>Sleep / Relax</li><li>Slimming</li><li>Sports</li><li>Stress / Mood</li><li>Women's Health</li>
    </ul>
  </aside>

  <aside class="sidebar" style="top:945px">
    <div class="filter-head"><span>Delivery</span>
      <svg width="9" height="9" viewBox="0 0 10 10"><circle cx="5" cy="5" r="4.3" fill="none" stroke="#333" stroke-width=".8"/><path d="M3 6 5 4 7 6" fill="none" stroke="#333" stroke-width=".8"/></svg></div>
    <ul class="filter-list">
      <li>Tablet</li><li>Liposomal</li><li>Suppository</li><li>Intravenous</li><li>Spray</li><li>Pump</li><li>Nebulised</li>
    </ul>
  </aside>

  <h2 class="section-title" style="top:252px">Vitamins</h2>
  <section class="product-row" style="top:294px">
    <div class="product-card" style="left:49px"><div class="product-photo" role="img" aria-label="Orange vegan supplement bottle"></div><p class="product-name">Flexa-Move™ Care<br>1500mg Glucosamine<br>x 180 tablets</p><p class="product-stars">★★★★★</p><p class="product-price"><small>from</small> $11.89</p><a class="btn btn-cart">Add to Cart</a></div>
    <div class="product-card" style="left:189px"><div class="product-photo" role="img" aria-label="Orange vegan supplement bottle"></div><p class="product-name">Flexa-Move™ Care<br>1500mg Glucosamine<br>x 180 tablets</p><p class="product-stars">★★★★★</p><p class="product-price"><small>from</small> $11.89</p><a class="btn btn-cart">Add to Cart</a></div>
    <div class="product-card" style="left:329px"><div class="product-photo" role="img" aria-label="Orange vegan supplement bottle"></div><p class="product-name">Flexa-Move™ Care<br>1500mg Glucosamine<br>x 180 tablets</p><p class="product-stars">★★★★★</p><p class="product-price"><small>from</small> $11.89</p><a class="btn btn-cart">Add to Cart</a></div>
    <div class="product-card" style="left:469px"><div class="product-photo" role="img" aria-label="Orange vegan supplement bottle"></div><p class="product-name">Flexa-Move™ Care<br>1500mg Glucosamine<br>x 180 tablets</p><p class="product-stars">★★★★★</p><p class="product-price"><small>from</small> $11.89</p><a class="btn btn-cart">Add to Cart</a></div>
  </section>
  <div class="see-more" style="top:458px">See More</div>

  <h2 class="section-title" style="top:490px">Nootropics</h2>
  <section class="product-row" style="top:532px">
    <div class="product-card" style="left:49px"><div class="product-photo" role="img" aria-label="Orange vegan supplement bottle"></div><p class="product-name">Flexa-Move™ Care<br>1500mg Glucosamine<br>x 180 tablets</p><p class="product-stars">★★★★★</p><p class="product-price"><small>from</small> $11.89</p><a class="btn btn-cart">Add to Cart</a></div>
    <div class="product-card" style="left:189px"><div class="product-photo" role="img" aria-label="Orange vegan supplement bottle"></div><p class="product-name">Flexa-Move™ Care<br>1500mg Glucosamine<br>x 180 tablets</p><p class="product-stars">★★★★★</p><p class="product-price"><small>from</small> $11.89</p><a class="btn btn-cart">Add to Cart</a></div>
    <div class="product-card" style="left:329px"><div class="product-photo" role="img" aria-label="Orange vegan supplement bottle"></div><p class="product-name">Flexa-Move™ Care<br>1500mg Glucosamine<br>x 180 tablets</p><p class="product-stars">★★★★★</p><p class="product-price"><small>from</small> $11.89</p><a class="btn btn-cart">Add to Cart</a></div>
    <div class="product-card" style="left:469px"><div class="product-photo" role="img" aria-label="Orange vegan supplement bottle"></div><p class="product-name">Flexa-Move™ Care<br>1500mg Glucosamine<br>x 180 tablets</p><p class="product-stars">★★★★★</p><p class="product-price"><small>from</small> $11.89</p><a class="btn btn-cart">Add to Cart</a></div>
  </section>
  <div class="see-more" style="top:696px">See More</div>

  <section class="about" role="img" aria-label="Faded background of a group yoga class meditating on mats">
    <h2 class="about-title">About Us</h2>
    <p>Lorem ipsum dolor sit amet, consectetur adipiscing elit. Phasellus non sodales ipsum. Pellentesque ac nisi eu sem suscipit luctus. Duis commodo aliquam mi, non pellentesque est finibus vitae. Maecenas ut faucibus magna, eget volutpat lorem. Nunc vestibulum ut nunc ut tincidunt. Curabitur non ante porttitor lectus volutpat imperdiet interdum sit amet erat. Maecenas convallis erat massa, sit amet faucibus purus imperdiet sed. Sed tellus odio, ullamcorper sed elit consequat, pretium dictum dui.</p>
    <p>Morbi a euismod sapien, ac porttitor sem. Suspendisse molestie at urna quis accumsan. Suspendisse potenti. Integer id dui elementum, feugiat erat quis, ultricies dolor. Quisque in ullamcorper purus, efficitur ultrices leo. Nullam non gravida nunc, eget interdum mi. Suspendisse ac nisi aliquet, tempus urna vitae, venenatis nibh. Vestibulum aliquet in tellus et aliquet. Praesent consequat arcu et mauris porttitor, ut lacinia dui lobortis. Praesent hendrerit dolor eu faucibus venenatis. Mauris porta auctor ex lacinia mollis. Morbi euismod massa a lacinia porttitor</p>
    <a class="btn btn-learn">Learn More</a>
  </section>

  <section class="contact">
    <h2 class="contact-title">Contact Us</h2>
    <p style="margin-top:18px">Get in touch for expert confidential supplement advice, or for customer services.</p>
    <p style="margin-top:12px;font-weight:700">Calling from the UK</p>
    <p>+44 20 7946 0321</p>
    <p>To contact us by email, please click the send us a message tab on the right.</p>
    <p>Our team is available</p>
    <p>Monday - Friday: 08:00 - 18:00</p>
    <p>Answer phone out of hours</p>
  </section>
  <a class="btn-message">Send us a message</a>

  <footer class="site-footer">
    <div class="footer-col" style="left:54px"><h4>Help &amp; Information</h4><ul><li>About Us</li><li>Careers at Northwick</li><li>Corporate Responsibility</li><li>Investors Site</li></ul></div>
    <div class="footer-col" style="left:246px"><h4>About Verdalis</h4><ul><li>About Us</li><li>Careers at Northwick</li><li>Corporate Responsibility</li><li>Investors Site</li></ul></div>
    <div class="footer-col" style="left:437px"><h4>More From Verdalis</h4><ul><li>About Us</li><li>Careers at Northwick</li><li>Corporate Responsibility</li><li>Investors Site</li></ul></div>
    <div class="footer-col" style="left:629px"><h4>Our Partners</h4><ul><li>About Us</li><li>Careers at Northwick</li><li>Corporate Responsibility</li><li>Investors Site</li></ul></div>
  </footer>

</div>
</body>
</html>
```